Orlent Telecom Business Card Competition

High quality international communications for consumers and business. We are re-designing our website and re-branding. Our current (old) website can be viewed at www.goorlent-example.net Vision statement - We enable people and communities to build and maintain strong and lasting global connections This is the brand image that we are trying to get across: •Quality—Orlent delivers the highest quality connections wherever you need to communicate. •Service—Orlent is always there for you, with the industry-leading service that promises to ensure that every experience is a good one. •Value—Orlent provides the best value in the global communications market. Typical messaging: Connecting the Most Important People in the World. Focus on international communications

We want to convey our service quality and that we really care about the service we provide and our customers. We want to emphasis the international aspect of our business. We want to make it personal, but it has to relate to business as well as individuals. We want the card to be unique in design but clear enough to read. We want a business prospect as well as a regular person to look at our card and know what we do.

Target Market(s)

Consumer - multi-ethnic consumer base living in the US calling, texting and connecting with family and friends in countries around the world 2. Busine

Industry/Entity Type

Communications

Requirements
Must have
• 1. Logo must be visible (see uploaded)

2.Artist can use variations of our company colors to accent our logo:

Hex Codes:
Magenta = ab3179
Blue = 2895c0
Green = 8ebb3f

3.Must have the following slogan visible: Because Every Voice Carries

below are the required data fields:

Full Name: Mark Tallow
Position: Chief Financial Officer
Office: +1 608-441-2871 ext.318
Mobile: +1 608-441-2871
Fax: +1 608-441-2871
Email: MarkT@goorlent-example.net
URL: www.goorlent-example.net
Address:
71820 Brindle Avenue
suite 412
Ashburn, VA 20163
USA

Nice to have
• Die cut cards or uniquely shaped cards would be interesting to see but not required

```html
<!DOCTYPE html>
<html lang="en">
<head>
<meta charset="utf-8">
<title>Orlent Telecom — Business Card</title>
<link rel="stylesheet" href="https://fonts.googleapis.com/css2?family=Cabin:wght@400;500&display=swap">
<style>
  :root {
    --magenta: #ab3179;
    --blue: #2895c0;
    --green: #8ebb3f;
    --ink: #111111;
    --black: #000000;
    --paper: #ffffff;
    --muted: #9a9a9a;
    --band-text: #bdbdbd;
    --grey-text: #555555;
    --stage: #ececec;
  }
  * { box-sizing: border-box; margin: 0; padding: 0; }
  html, body { width: 1200px; height: 1000px; overflow: hidden; }
  body {
    position: relative;
    background: var(--stage);
    font-family: "Cabin", "Gill Sans", sans-serif;
    color: var(--ink);
  }
  .card {
    position: absolute;
    border-radius: 16px;
    overflow: hidden;
    box-shadow: 0 6px 14px rgba(0,0,0,0.25);
  }

  /* Front */
  .card-front {
    left: 27px; top: 20px; width: 677px; height: 381px;
    background: var(--black);
  }
  .card-front .wordmark {
    position: absolute; left: 0; right: 0; top: 290px;
    text-align: center;
    font-size: 32px; font-weight: 500; letter-spacing: 0.5px;
    color: var(--paper);
  }

  /* Back */
  .card-back {
    left: 27px; top: 486px; width: 677px; height: 381px;
    background: var(--paper);
  }
  .card-back .side-band {
    position: absolute; left: 0; top: 0; width: 162px; height: 100%;
    background: var(--black);
  }
  .card-back .holder {
    position: absolute; left: 0; width: 144px; top: 11px; text-align: right;
  }
  .card-back .holder .name { font-size: 18px; color: var(--band-text); white-space: nowrap; }
  .card-back .holder .role { font-size: 9.5px; color: var(--band-text); margin-top: 1px; white-space: nowrap; }
  .card-back .brand {
    position: absolute; left: 162px; width: 300px; top: 160px; text-align: center;
  }
  .card-back .brand .wordmark {
    font-size: 30px; font-weight: 500; color: var(--ink);
  }
  .card-back .brand .slogan {
    font-size: 13px; color: var(--muted); margin-top: 20px;
  }
  .contact-list {
    position: absolute; left: 482px; top: 163px; list-style: none;
    font-size: 13px; color: var(--ink);
  }
  .contact-list li { display: flex; height: 25.5px; }
  .contact-list .label { width: 22px; color: var(--magenta); }
  .contact-list li.address { margin-top: 11px; line-height: 18px; height: auto; }

  /* Landscape variant */
  .card-variant {
    left: 800px; top: 126px; width: 360px; height: 215px;
    background: var(--paper); border-radius: 0;
    box-shadow: 0 4px 10px rgba(0,0,0,0.15);
  }
  .card-variant .corner { position: absolute; right: 0; top: 0; }
  .card-variant .wordmark {
    position: absolute; left: 18px; top: 40px;
    font-size: 21px; font-weight: 500; color: var(--ink);
  }
  .card-variant .slogan {
    position: absolute; right: 14px; top: 94px;
    font-size: 10px; color: #b5b5b5;
  }
  .card-variant .name { position: absolute; left: 20px; top: 96px; font-size: 16px; }
  .card-variant .role { position: absolute; left: 20px; top: 117px; font-size: 8px; color: var(--grey-text); }
  .mini-list {
    position: absolute; top: 138px; list-style: none; font-size: 9.5px;
  }
  .mini-list li { display: flex; align-items: flex-start; height: 17.5px; }
  .mini-list.left { left: 19px; }
  .mini-list.right { left: 187px; }
  .tag {
    display: inline-block; width: 11px; height: 11px; border-radius: 2px;
    color: var(--paper); font-size: 7px; line-height: 11px; text-align: center;
    margin-right: 4px; flex: none;
  }
  .tag.blue { background: var(--blue); }
  .tag.magenta { background: var(--magenta); }
  .tag.green { background: var(--green); }
</style>
</head>
<body>

  <section class="card card-front" aria-label="Card front">
    <div class="wordmark">Orlent Telecom</div>
  </section>

  <section class="card card-back" aria-label="Card back">
    <div class="side-band"></div>
    <div class="holder">
      <div class="name">Mark Tallow</div>
      <div class="role">Chief Financial Officer</div>
    </div>
    <div class="brand">
      <div class="wordmark">Orlent Telecom</div>
      <div class="slogan">‘Because Every Voice Carries’</div>
    </div>
    <ul class="contact-list">
      <li><span class="label">T</span>+1 608-441-2871 ext.318</li>
      <li><span class="label">M</span>+1 608-441-2871</li>
      <li><span class="label">F</span>+1 608-441-2871</li>
      <li><span class="label">E</span>MarkT@goorlent-example.net</li>
      <li><span class="label">W</span>www.goorlent-example.net</li>
      <li class="address"><span class="label">A</span><span>71820 Brindle Avenue<br>suite 412<br>Calder Falls, WI 53717</span></li>
    </ul>
  </section>

  <section class="card card-variant" aria-label="Landscape card variant">
    <svg class="corner" width="142" height="88" viewBox="218 0 142 88" aria-hidden="true">
      <path d="M218 0 H360 V88 H272 Q240 86 232 52 Q226 22 218 0 Z" fill="var(--blue)"/>
    </svg>
    <div class="wordmark">Orlent Telecom</div>
    <div class="slogan">‘Because Every Voice Carries’</div>
    <div class="name">Mark Tallow</div>
    <div class="role">Chief Financial Officer</div>
    <ul class="mini-list left">
      <li><span class="tag blue">T</span>+1 608-441-2871 ext.318</li>
      <li><span class="tag magenta">M</span>+1 608-441-2871</li>
      <li><span class="tag green">F</span>+1 608-441-2871</li>
    </ul>
    <ul class="mini-list right">
      <li><span class="tag blue">E</span>MarkT@goorlent-example.net</li>
      <li><span class="tag magenta">W</span>www.goorlent-example.net</li>
      <li><span class="tag green">A</span><span>71820 Brindle Avenue suite 412<br>Calder Falls, WI 53717</span></li>
    </ul>
  </section>

</body>
</html>
```